Business cards for Harbourline Supply Pty Ltd that import building products into Australia from China
Target Market(s)
Business to Business
Industry/Entity Type
Business
Contact Information for Business Card
Front: Logo and Business Name
Rear:
Vernon Ashcombe
General Manager
Mobile: 0427 619 354
email: vern@harbourlinesupply.com.au
alternative email: vern@coastwardgoods.com.au
web: www.harbourlinesupply.com.au
Adelaide, Brisbane and Darwin
Colors
ec1f27
fbee3d

```html
<!DOCTYPE html>
<html lang="en">
<head>
<meta charset="utf-8">
<title>Harbourline Supply – Business Cards</title>
<link rel="stylesheet" href="https://fonts.googleapis.com/css2?family=Arimo:wght@400&family=Barlow+Semi+Condensed:wght@500;600&display=swap">
<style>
  :root {
    --brand-red: #e31b23;
    --brand-yellow: #ffde00;
    --label-yellow: #fbee3d;
    --ink-white: #ffffff;
    --backdrop: #3d2a20;
  }
  * { margin: 0; padding: 0; box-sizing: border-box; }
  html, body {
    width: 1200px;
    height: 448px;
    overflow: hidden;
    background: var(--backdrop);
  }
  .canvas {
    position: relative;
    width: 1200px;
    height: 448px;
  }
  .card {
    position: absolute;
    top: 67px;
    width: 549px;
    height: 313px;
  }
  .card--rear {
    left: 39px;
    background: var(--brand-red);
    color: var(--ink-white);
    text-align: center;
  }
  .card--front {
    left: 612px;
    background: var(--brand-yellow);
    display: flex;
    align-items: center;
    justify-content: center;
  }
  .person {
    position: absolute;
    top: 50px;
    left: 0;
    right: 0;
    font-family: "Barlow Semi Condensed", sans-serif;
    text-transform: uppercase;
    line-height: 1;
  }
  .person__name {
    font-weight: 600;
    font-size: 30px;
    letter-spacing: 0.3px;
  }
  .person__role {
    font-weight: 500;
    font-size: 20px;
    margin-top: 4px;
    letter-spacing: 0.4px;
  }
  .contact {
    position: absolute;
    top: 139px;
    left: 0;
    right: 0;
    display: flex;
    flex-direction: column;
    align-items: center;
    font-family: "Arimo", sans-serif;
    font-size: 19.5px;
    line-height: 25px;
  }
  .contact__row {
    display: flex;
    gap: 6px;
    text-align: left;
  }
  .contact__row + .contact__row { margin-top: 14px; }
  .contact__row--website { margin-top: 11px !important; }
  .contact__label { color: var(--label-yellow); }
  .contact__values { color: var(--ink-white); }
  .brand-name {
    font-family: "Arimo", sans-serif;
    font-weight: 400;
    font-size: 46px;
    color: var(--brand-red);
    letter-spacing: 0.5px;
  }
</style>
</head>
<body>
<main class="canvas">
  <section class="card card--rear" aria-label="Card rear: contact details">
    <header class="person">
      <h1 class="person__name">Vernon Ashcombe</h1>
      <p class="person__role">General Manager</p>
    </header>
    <div class="contact">
      <p class="contact__row">
        <span class="contact__label">Mobile:</span>
        <span class="contact__values">0427 619 354</span>
      </p>
      <p class="contact__row">
        <span class="contact__label">Email:</span>
        <span class="contact__values">vern@harbourlinesupply.com.au<br>vern@coastwardgoods.com.au</span>
      </p>
      <p class="contact__row contact__row--website">
        <span class="contact__label">Website:</span>
        <span class="contact__values">www.harbourlinesupply.com.au</span>
      </p>
    </div>
  </section>

  <section class="card card--front" aria-label="Card front: business name">
    <p class="brand-name">harbourline supply</p>
  </section>
</main>
</body>
</html>
```